Speisekarten-Design für SportsBar
Zielgruppe
Wir sind moderne SportsBar eines 2.Bundesligisten mit breitem Publikum auch ausserhalb der Fussballs. Wir haben Salate, Burger, Schnitzel und Steaks sowie eine gut sortierte Getränkekarte.
Aufgabenstellung
Für unsere Restaurant Ahornstube SportsBar suchen wir eine neue Speisekarte (Alte Speisekarte ist angehängt)
Wir haben uns für das Format A4 im Clipboard entschieden, da wir flexibel sein möchten, auch wenn sich mal etwas ändern sollte, wir somit eine Seite austauschen können. Auch wollen wir mit einer Wochenkarte arbeiten, die auf der zweiten Seite anhängen sollte.
Wir wünschen uns ein sportlich modernes Design, mit Speisefotos und Sportfotos im Mix als Eyecatcher.
Die Seite für den Kaffe wird nicht benötigt, da wir diese von unserem Partner als fertige Vorlage bekommen(Seite hängt an).
Logos der Getränkemarken sind ebenfalls im Anhang. Aller anderen Fotos etc. können sofort bei Bedarf geliefert werden.
Für den ersten Entwurf würde ich gerne 3-5 Seiten sehen wollen, dabei sind wichtig !
- Titelseite
- Brunch & Buffetseite
- Schnitzelseite
- Burgerseite
- Getränke(Bier)
Vielen Dank, für fragen stehe ich jederzeit zur Verfügung

```html
<!DOCTYPE html>
<html lang="de">
<head>
<meta charset="utf-8">
<title>Schon gewusst? – Feiern</title>
<link rel="stylesheet" href="https://fonts.googleapis.com/css2?family=Carlito:wght@400;700&family=Indie+Flower&display=swap">
<style>
  :root {
    --turf-base: #4f6b90;
    --turf-dark: #2f4565;
    --band: #303749;
    --text: #ffffff;
    --frame: #ffffff;
  }
  html, body { margin: 0; padding: 0; overflow: hidden; }
  body { width: 848px; height: 1200px; }
  .page {
    position: relative;
    width: 848px;
    height: 1200px;
    overflow: hidden;
    background: var(--turf-base);
    font-family: "Carlito", "Calibri", sans-serif;
    color: var(--text);
  }
  .turf {
    position: absolute;
    left: 0; top: 0;
    width: 848px; height: 1200px;
  }
  .title-band {
    position: absolute;
    left: 0; top: 65px;
    width: 848px; height: 72px;
    background: var(--band);
    display: flex; align-items: center; justify-content: center;
  }
  .title-band h1 {
    margin: 0;
    font-family: "Indie Flower", cursive;
    font-weight: 400;
    font-size: 38px;
    letter-spacing: 1.5px;
  }
  .intro {
    position: absolute;
    left: 40px; top: 172px;
    width: 800px;
    text-shadow: 0 1px 2px rgba(20, 30, 50, 0.6);
  }
  .intro h2 {
    margin: 0 0 20px;
    padding-right: 32px;
    text-align: center;
    font-size: 20px;
    font-weight: 700;
  }
  .intro p {
    margin: 0 0 24px;
    font-size: 17.2px;
    line-height: 24px;
    white-space: nowrap;
  }
  .photo-stack {
    position: absolute;
    left: 0; top: 0;
    width: 848px; height: 1200px;
  }
</style>
</head>
<body>
<main class="page">
  <svg class="turf" width="848" height="1200" viewBox="0 0 848 1200" aria-hidden="true">
    <defs>
      <filter id="turfGrain" x="0" y="0" width="100%" height="100%">
        <feTurbulence type="fractalNoise" baseFrequency="0.85" numOctaves="3" seed="7" result="noise"/>
        <feColorMatrix in="noise" type="matrix"
          values="0 0 0 0 0.78
                  0 0 0 0 0.84
                  0 0 0 0 0.93
                  0 0 0 1.6 -0.75" />
      </filter>
      <filter id="turfShade" x="0" y="0" width="100%" height="100%">
        <feTurbulence type="fractalNoise" baseFrequency="1.3" numOctaves="2" seed="3" result="noise"/>
        <feColorMatrix in="noise" type="matrix"
          values="0 0 0 0 0.12
                  0 0 0 0 0.18
                  0 0 0 0 0.28
                  0 0 0 1.8 -0.8" />
      </filter>
      <linearGradient id="turfFade" x1="0" y1="0" x2="0" y2="1">
        <stop offset="0" stop-color="#2f4565" stop-opacity="0.35"/>
        <stop offset="0.15" stop-color="#2f4565" stop-opacity="0"/>
        <stop offset="0.85" stop-color="#2f4565" stop-opacity="0"/>
        <stop offset="1" stop-color="#2f4565" stop-opacity="0.4"/>
      </linearGradient>
    </defs>
    <rect width="848" height="1200" fill="var(--turf-base)"/>
    <rect width="848" height="1200" filter="url(#turfShade)"/>
    <rect width="848" height="1200" filter="url(#turfGrain)"/>
    <rect width="848" height="1200" fill="url(#turfFade)"/>
  </svg>

  <header class="title-band">
    <h1>Schon gewusst ?</h1>
  </header>

  <section class="intro">
    <h2>Sie Feiern – Wir machen !</h2>
    <p>Sie haben einen Anlass zum Feiern und möchten sich um nichts kümmern sondern sich einfach<br>mit Ihren Gästen amüsieren und bedienen lassen ?</p>
    <p>Ob Geburtstag, Firmenfeier, Jubiläum oder ein Geschäftsessen. Wir nehmen uns gerne die Zeit<br>um Sie im Vorfeld umfassend über Ihre Möglichkeiten zu beraten. Von der Menüwahl über die<br>Getränkewahl bis hin zu den Tischdekorationen.</p>
    <p>So können wir Ihre Vorstellungen und Wünsche optimal umsetzen und Ihre Feier für Sie und<br>Ihre Gäste zu einem unvergesslichen Erlebnis werden lassen.</p>
  </section>

  <svg class="photo-stack" width="848" height="1200" viewBox="0 0 848 1200">
    <defs>
      <clipPath id="dinnerClip"><polygon points="465,460 860,532 860,884 410,732"/></clipPath>
      <clipPath id="toastClip"><polygon points="0,787 573,715 609,1053 0,1149"/></clipPath>
      <linearGradient id="dinnerBase" x1="0" y1="0" x2="0" y2="1">
        <stop offset="0" stop-color="#e7c9a0"/>
        <stop offset="0.35" stop-color="#a2704c"/>
        <stop offset="0.7" stop-color="#6a4634"/>
        <stop offset="1" stop-color="#8a5a38"/>
      </linearGradient>
      <linearGradient id="toastBase" x1="0" y1="0" x2="1" y2="1">
        <stop offset="0" stop-color="#c9c2b8"/>
        <stop offset="0.4" stop-color="#d8b89a"/>
        <stop offset="0.75" stop-color="#9c7260"/>
        <stop offset="1" stop-color="#5e4a44"/>
      </linearGradient>
      <radialGradient id="warmGlow">
        <stop offset="0" stop-color="#fbe3bd" stop-opacity="0.9"/>
        <stop offset="1" stop-color="#fbe3bd" stop-opacity="0"/>
      </radialGradient>
      <radialGradient id="deepShade">
        <stop offset="0" stop-color="#2e211c" stop-opacity="0.75"/>
        <stop offset="1" stop-color="#2e211c" stop-opacity="0"/>
      </radialGradient>
      <radialGradient id="redAccent">
        <stop offset="0" stop-color="#8e2b2b" stop-opacity="0.7"/>
        <stop offset="1" stop-color="#8e2b2b" stop-opacity="0"/>
      </radialGradient>
      <radialGradient id="blueAccent">
        <stop offset="0" stop-color="#3f5677" stop-opacity="0.8"/>
        <stop offset="1" stop-color="#3f5677" stop-opacity="0"/>
      </radialGradient>
      <radialGradient id="paleLight">
        <stop offset="0" stop-color="#f6f1ea" stop-opacity="0.9"/>
        <stop offset="1" stop-color="#f6f1ea" stop-opacity="0"/>
      </radialGradient>
    </defs>

    <polygon class="photo-frame" points="415,499 900,580 860,935 380,739" fill="none" stroke="var(--frame)" stroke-width="1.5"/>
    <g class="photo" clip-path="url(#dinnerClip)" role="img" aria-label="Foto: Freunde lachen gemeinsam an einem gedeckten Restauranttisch">
      <rect x="400" y="450" width="460" height="440" fill="url(#dinnerBase)"/>
      <ellipse cx="640" cy="520" rx="220" ry="70" fill="url(#warmGlow)"/>
      <ellipse cx="470" cy="640" rx="80" ry="140" fill="url(#deepShade)"/>
      <ellipse cx="590" cy="690" rx="70" ry="60" fill="url(#redAccent)"/>
      <ellipse cx="780" cy="650" rx="90" ry="80" fill="url(#blueAccent)"/>
      <ellipse cx="700" cy="800" rx="160" ry="50" fill="url(#deepShade)"/>
    </g>

    <polygon class="photo-frame" points="-10,760 578,676 629,1029 -10,1125" fill="none" stroke="var(--frame)" stroke-width="1.5"/>
    <g class="photo" clip-path="url(#toastClip)" role="img" aria-label="Foto: Gäste stoßen mit Weingläsern über einem Tisch mit Brot und Speisen an">
      <rect x="0" y="700" width="620" height="460" fill="url(#toastBase)"/>
      <ellipse cx="260" cy="790" rx="220" ry="60" fill="url(#paleLight)"/>
      <ellipse cx="470" cy="820" rx="90" ry="80" fill="url(#warmGlow)"/>
      <ellipse cx="220" cy="910" rx="70" ry="35" fill="url(#redAccent)"/>
      <ellipse cx="60" cy="960" rx="80" ry="120" fill="url(#deepShade)"/>
      <ellipse cx="530" cy="980" rx="80" ry="70" fill="url(#blueAccent)"/>
      <ellipse cx="280" cy="1080" rx="220" ry="60" fill="url(#deepShade)"/>
    </g>
  </svg>
</main>
</body>
</html>
```